Cell phone case packaging

Looking to have our own cell phone case packaging design. The pakaging will hold smart phone case. Looking for something that would fit an 8 x 10 size. The packaging should match the colors of this website www.brimvalemobile.com.

In the back i would like to have the definition of the work Joy.

Joie: Sentiment de plaisir, de bonheur intense, caractérisé par sa plénitude et sa durée limitée, et éprouvé par quelqu'un dont une aspiration, un désir est satisfait ou en voie de l'être

Joy: the emotion of great delight or happiness caused by something exceptionally good or satisfying; keen pleasure; elation

I prefer a clam shell design. I have attach examples of packaging designs i like

Industry/Entity Type

Wireless Communication

Font styles to use
Sans Serif

Colors
0255a3
33b8a4
fece3e
f04a50

Requirements
Must have
• 1. Ability to feel the texture of the case
• 2. must be all in french
• 3. very colorful
• 3. must be able to place on hook

```html
<!DOCTYPE html>
<html lang="fr">
<head>
<meta charset="utf-8">
<title>Joie — emballage arrière</title>
<link href="https://fonts.googleapis.com/css2?family=Open+Sans:ital,wght@0,300;0,400;1,400&display=swap" rel="stylesheet">
<style>
  :root {
    --sun: #fde84c;
    --sun-soft: #fbf1a0;
    --peach: #f4a26a;
    --coral: #f07070;
    --magenta: #ec2c71;
    --rose: #ef6c97;
    --blush: #f6b3c8;
    --mauve: #b486ad;
    --haze: #b9c3e0;
    --sky: #3cb8e2;
    --card: #ffffff;
    --card-shade: #f1f1f1;
    --card-edge: #8f8f8f;
    --ink: #222222;
  }
  html, body {
    margin: 0;
    padding: 0;
    width: 960px;
    height: 1200px;
    overflow: hidden;
    background: #ffffff;
  }
  .package-back {
    position: relative;
    width: 960px;
    height: 1200px;
    overflow: hidden;
    font-family: "Open Sans", Arial, sans-serif;
  }
  .lattice-pattern {
    position: absolute;
    inset: 0;
    background:
      linear-gradient(180deg,
        var(--sun) 0%,
        var(--sun-soft) 14%,
        var(--peach) 24%,
        var(--coral) 33%,
        var(--magenta) 45%,
        var(--rose) 58%,
        var(--blush) 68%,
        var(--mauve) 78%,
        var(--haze) 87%,
        var(--sky) 100%);
  }
  .definition-card {
    position: absolute;
    left: 94px;
    top: 894px;
    width: 775px;
    height: 255px;
    box-sizing: border-box;
    background: linear-gradient(180deg, var(--card) 0%, var(--card) 60%, var(--card-shade) 100%);
    border: 2px solid var(--card-edge);
    border-radius: 36px;
    box-shadow: 0 2px 6px rgba(0, 0, 0, 0.25);
    text-align: center;
    color: var(--ink);
    padding-top: 22px;
  }
  .definition-word {
    margin: 0;
    font-style: italic;
    font-weight: 400;
    font-size: 51px;
    line-height: 52px;
  }
  .definition-text {
    margin: 0;
    font-weight: 300;
    font-size: 29px;
    line-height: 36px;
    white-space: nowrap;
  }
</style>
</head>
<body>
  <main class="package-back">
    <div class="lattice-pattern" role="img" aria-label="Motif décoratif de gouttes entrelacées en relief, en dégradé jaune, rose et bleu sur fond blanc"></div>
    <section class="definition-card">
      <h1 class="definition-word">Joie</h1>
      <p class="definition-text">Sentiment de plaisir, de bonheur intense, caractérisé<br>par sa plénitude et sa durée limitée, et éprouvé par<br>quelqu'un dont une aspiration, un désir est satisfait<br>ou en voie de l'être</p>
    </section>
  </main>
</body>
</html>
```